1940s Weekend Poster for Tourist Attraction - United Kingdom

We need a professional and stylish poster designing for our 1940s Weekend. This is the first time we have run the event and it therefore needs to be professional, eye catching and draw customers in.

The weekend is a 1940s themed event, featuring battles, vehicles, musical entertainment, so the final design should reflect this. It needs to feel nostalgic and reflect the event. We are based in the UK, so union jack, bunting etc. We have attached some example posters we like as a source of possible inspiration.

Target Market(s)

Families, re-enactors, enthusiasts.

Industry/Entity Type

Event

Font styles to use
Sans Serif
Decorative

Requirements
Must have
• The following text:
• "Harrowmere Valley Steam Tramway presents
• Harrowmere 1940's Weekend - 13th & 14th August 2016
• Come along, put your glad rags on and relive all things 1940s - with live entertainment, battle re-enactments, military vehicles and much more!
• Further details at www.harrowmere1940s.co.uk or phone 01638 927314"
Nice to have
• Stylish imagery - needs to be eyecatching.
Should not have
• Clipart!

```html
<!DOCTYPE html>
<html lang="en">
<head>
<meta charset="utf-8">
<title>Harrowmere 1940's Weekend</title>
<link rel="stylesheet" href="https://fonts.googleapis.com/css2?family=Federo&family=Limelight&family=Special+Elite&display=swap">
<style>
  :root {
    --page: #f1f1f1;
    --flag-white: #eceaed;
    --flag-blue: #5470c4;
    --flag-blue-deep: #3e58ad;
    --flag-red: #e4475d;
    --flag-red-soft: #ec7f8c;
    --title-blue: #24348f;
    --ink: #1d1a2c;
  }
  html, body {
    margin: 0;
    width: 1200px;
    height: 1200px;
    overflow: hidden;
    background: var(--page);
  }
  .poster {
    position: absolute;
    left: 216px;
    top: 30px;
    width: 768px;
    height: 1140px;
    box-shadow: 0 2px 10px rgba(0,0,0,0.12);
  }
  .presents { font-family: "Special Elite", "Courier New", monospace; font-size: 22px; fill: var(--ink); }
  .headline { font-family: "Federo", "Poiret One", sans-serif; fill: var(--title-blue); }
  .event-date { font-family: "Limelight", serif; font-size: 30px; fill: var(--ink); }
  .invite { font-family: "Limelight", serif; fill: var(--ink); }
  .invite .big { font-size: 34px; }
  .invite .small { font-size: 24px; }
  .details { font-family: "Limelight", serif; font-size: 20px; fill: var(--ink); }
</style>
</head>
<body>
<svg class="poster" viewBox="0 0 694 1030" xmlns="http://www.w3.org/2000/svg">
  <defs>
    <path id="arc-presents" d="M 70 170 A 420 420 0 0 1 624 170"/>
    <path id="arc-date" d="M 110 400 A 335 335 0 0 0 580 400"/>
  </defs>

  <g class="flag-collage" role="img" aria-label="Union flag overlaid with red and blue tinted 1940s photographs of crowds, vintage vehicles and period dress">
    <rect width="694" height="1030" fill="var(--flag-blue)"/>
    <rect x="0" y="0" width="694" height="1030" fill="var(--flag-blue-deep)" opacity="0.25"/>
    <line x1="0" y1="0" x2="694" y2="1030" stroke="var(--flag-white)" stroke-width="120"/>
    <line x1="694" y1="0" x2="0" y2="1030" stroke="var(--flag-white)" stroke-width="120"/>
    <line x1="0" y1="0" x2="694" y2="1030" stroke="var(--flag-red-soft)" stroke-width="38"/>
    <line x1="694" y1="0" x2="0" y2="1030" stroke="var(--flag-red-soft)" stroke-width="38"/>
    <rect x="300" y="0" width="165" height="1030" fill="var(--flag-white)"/>
    <rect x="0" y="365" width="694" height="290" fill="var(--flag-white)"/>
    <rect x="338" y="0" width="88" height="1030" fill="var(--flag-red)"/>
    <rect x="0" y="425" width="694" height="170" fill="var(--flag-red)"/>
  </g>

  <text class="presents"><textPath href="#arc-presents" startOffset="50%" text-anchor="middle">Harrowmere Valley Steam Tramway presents</textPath></text>

  <text class="headline" x="125" y="190" font-size="60" textLength="430" lengthAdjust="spacingAndGlyphs">HARROWMERE</text>
  <text class="headline" x="115" y="295" font-size="124" textLength="445" lengthAdjust="spacingAndGlyphs">1940'S</text>
  <text class="headline" x="115" y="382" font-size="76" textLength="445" lengthAdjust="spacingAndGlyphs">WEEKEND</text>

  <text class="event-date"><textPath href="#arc-date" startOffset="50%" text-anchor="middle">13TH &amp; 14TH AUGUST 2016</textPath></text>

  <g class="invite">
    <text x="8" y="600" textLength="545" lengthAdjust="spacingAndGlyphs"><tspan class="big">COME ALONG,</tspan><tspan class="small"> PUT YOUR GLAD RAGS ON</tspan></text>
    <text x="8" y="648" textLength="545" lengthAdjust="spacingAndGlyphs"><tspan class="small">AND </tspan><tspan class="big">RELIVE ALL THINGS 1940S</tspan></text>
    <text x="8" y="696" textLength="535" lengthAdjust="spacingAndGlyphs"><tspan class="small">WITH </tspan><tspan class="big">LIVE ENTERTAINMENT,</tspan><tspan class="small"> BATTLE</tspan></text>
    <text x="8" y="744" textLength="545" lengthAdjust="spacingAndGlyphs"><tspan class="small">RE-ENACTMENTS, </tspan><tspan class="big">MILITARY VEHICLES</tspan></text>
    <text x="8" y="796"><tspan class="big">AND MUCH MORE!</tspan></text>
  </g>

  <g class="details">
    <text x="8" y="846">FURTHER DETAILS AT WWW.HARROWMERE1940S.CO.UK</text>
    <text x="8" y="876">OR PHONE 01638 927314</text>
  </g>
</svg>
</body>
</html>
```